Business Card Design

General Brief:
Varnel Works is a newly established international manufacturing company. We have a manufacturing facility in China and are in the process of building a new facility in Brazil and are expanding into Africa, the Middle East and Western markets by marketing our products through a licensee program. We use production line manufacture processes (similar to the automotive industry) to produce houses, apartments, hotels and accommodation for the resource sector. We will need to be able to differentiate between the various regions that we serve and the market we operate in.

Key Words to describe our business:
International, Global, Professional, Quality, Standard Compliant, Designful, Cost Effective, Experienced

General Brief:
We need business card designs which cater for the possibility of differentiating the various regions that we serve and the market we operate in. Also, we need a secondary typography selection which suits the primary typography used in the corporate signature (please always state which font is being applied so as to cross-check for the necessary font licenses). First print will be made for our Chinese head office and division, therefore will have the special prerequisite of featuring two distinct languages: English-speaking and Chinese. We assume that a double sided version (recto/verso) could work best in order to separate the languages—other creative interpretations, options and integrations are welcome.

Logo Symbolism:
A dot might seem to be an unassuming little thing, the first mark on the pristine sheet of paper. In this case, the dot is a beginning. But see what just happened there? The dot, an essential component in the structure of the sentence, closed it, making it a symbol of ending. Therefore, the dot is both an origination and a conclusion, encompassing all the possibilities of the universe within it, a seed full of potential and a symbol of the supreme being. The dot is also called the "bindhu," which means "drop." The bindhu is a symbol of the absolute, marked on the forehead at the position of the third eye in the place believed to be the seat of the soul. The presence of dots outside or within a symbol can signify the presence of something else. It also acts as reminder of the concept of space and all in all performs as a very positive symbol in the Varnel Works logo.

Target Market(s)

See Stationary Project

Industry/Entity Type

Accommodation

Requirements
Must have
• See Stationary Project

Logo on Stationary Project

```html
<!DOCTYPE html>
<html lang="en">
<head>
<meta charset="utf-8">
<title>Varnel Works — Business Card</title>
<link rel="stylesheet" href="https://fonts.googleapis.com/css2?family=Questrial&family=Montserrat:wght@700&display=swap">
<style>
  :root {
    --backdrop: #4a4a4a;
    --paper: #f4f4f4;
    --navy: #0f2c3a;
    --navy-deep: #0a1f2a;
    --accent: #1b8fd6;
    --slate: #6d737a;
    --ink: #1c3c4c;
    --white: #ffffff;
  }
  html, body {
    margin: 0;
    padding: 0;
    width: 1200px;
    height: 1000px;
    overflow: hidden;
    background: var(--backdrop);
  }
  .canvas {
    position: relative;
    width: 1200px;
    height: 1000px;
    font-family: "Questrial", "Century Gothic", sans-serif;
  }
  .card {
    position: absolute;
    width: 528px;
    height: 302px;
    border-radius: 14px;
    overflow: hidden;
    box-shadow: 0 6px 14px rgba(0,0,0,0.35);
  }
  .card--front { left: 192px; top: 173px; background: var(--paper); color: var(--ink); }
  .card--back  { left: 487px; top: 558px; background: linear-gradient(180deg, var(--navy) 0%, var(--navy-deep) 100%); }

  .wordmark {
    position: absolute;
    font-size: 36px;
    letter-spacing: 0.3px;
    line-height: 1;
    white-space: nowrap;
  }
  .card--front .wordmark { left: 38px; top: 62px; color: var(--navy); }
  .card--back .wordmark { right: 60px; top: 124px; color: var(--white); }

  .holder { position: absolute; right: 35px; top: 67px; text-align: right; }
  .holder__name { font-family: "Montserrat", sans-serif; font-weight: 700; font-size: 15px; letter-spacing: 0.6px; color: var(--navy); }
  .holder__role { font-size: 12px; color: var(--ink); margin-top: 1px; }

  .contact { position: absolute; top: 224px; font-size: 13px; line-height: 20px; }
  .contact--address { right: 342px; text-align: right; }
  .contact--phones { left: 214px; }
  .contact--web { right: 35px; }
  .contact__row { display: flex; align-items: center; gap: 8px; white-space: nowrap; }
  .contact__icon { width: 12px; height: 12px; flex: none; }

  .strip { position: absolute; left: 0; bottom: 0; height: 22px; }
  .strip--slate { width: 198px; background: var(--slate); }
  .strip--navy { left: 200px; width: 328px; background: var(--navy); }

  .back-decor { position: absolute; inset: 0; }
</style>
</head>
<body>
<main class="canvas">

  <section class="card card--front" aria-label="Card front">
    <div class="wordmark">Varnel Works</div>

    <div class="holder">
      <div class="holder__name">MARA LINDQVIST</div>
      <div class="holder__role">Manager</div>
    </div>

    <div class="contact contact--address">
      <div>Halden Forge Road</div>
      <div>Northbrook NSW 2790</div>
    </div>

    <div class="contact contact--phones">
      <div class="contact__row">
        <svg class="contact__icon" viewBox="0 0 12 12"><circle cx="6" cy="6" r="5.4" fill="none" stroke="var(--accent)" stroke-width="1"/><path d="M4.2 3.2l1 1-0.6 0.7c0.4 0.9 1 1.5 1.9 1.9l0.7-0.6 1 1-0.8 0.8C5.6 7.7 4.3 6.4 3.4 4z" fill="var(--accent)"/></svg>
        <span>+61 2 5550 1420</span>
      </div>
      <div class="contact__row">
        <svg class="contact__icon" viewBox="0 0 12 12"><circle cx="6" cy="6" r="5.4" fill="none" stroke="var(--accent)" stroke-width="1"/><rect x="3.5" y="5" width="5" height="3" fill="var(--accent)"/><rect x="4.3" y="3.4" width="3.4" height="1.4" fill="var(--accent)"/></svg>
        <span>+61 2 5550 1430</span>
      </div>
    </div>

    <div class="contact contact--web">
      <div class="contact__row">
        <svg class="contact__icon" viewBox="0 0 12 12"><circle cx="6" cy="6" r="5.4" fill="none" stroke="var(--accent)" stroke-width="1"/><rect x="3.3" y="4" width="5.4" height="4" fill="var(--accent)"/><path d="M3.3 4l2.7 2 2.7-2" fill="none" stroke="var(--paper)" stroke-width="0.7"/></svg>
        <span>info@varnelworks.com</span>
      </div>
      <div class="contact__row">
        <svg class="contact__icon" viewBox="0 0 12 12" fill="none" stroke="var(--accent)" stroke-width="1"><circle cx="6" cy="6" r="5.4"/><ellipse cx="6" cy="6" rx="2.3" ry="5.4"/><path d="M0.6 6h10.8M1.5 3.3h9M1.5 8.7h9"/></svg>
        <span>www.varnelworks.com</span>
      </div>
    </div>

    <div class="strip strip--slate"></div>
    <div class="strip strip--navy"></div>
  </section>

  <section class="card card--back" aria-label="Card back">
    <svg class="back-decor" viewBox="0 0 528 302" aria-hidden="true">
      <circle cx="162" cy="153" r="44" fill="rgba(255,255,255,0.05)"/>
      <path d="M0 165 A125 125 0 0 1 125 290 L125 302 L84 302 L84 290 A84 84 0 0 0 0 206 Z" fill="rgba(255,255,255,0.04)"/>
    </svg>
    <div class="wordmark">Varnel Works</div>
  </section>

</main>
</body>
</html>
```